"tide-LOOP." SoCal's Fishing Industry's single stop for the latest products, content, and services

Hi, looking for a website design for new LA based company called "tide-LOOP." Where we showcase all the latest and greatest products, services, and content in a highly visually appealing platform for all fishing manufacturers and service providers as they relate to the fishing community (manufactures and service providers pay for cost-tiered content exposure and marketing, free exposure for manufacturers and service providers will have affiliate marketing link at minimal content exposure). As well, looking to include an in-site blog, store-products, and media content such as articles, video edits, and fishing condition picture galleries. Visually, looking for a minimalist/clean/blocked/ filterable and visually captivating gallery. Looking for a color pallet with white-background, deep blue- primary, light gray- secondary, light sky blue- third. Style- cleanliness and structure of wirestack.example meets content like mkharborline.example.

Target Market(s)

Primary- Southern California/Southwest Fishing Community, Secondary- All other US Fishing Communities

Coding

Coded - Design and coding required

Number of Pages Required

5+ page

Font styles to use
Sans Serif

Colors
959595
86cfc6
cadf82
333333
0555a3

Requirements
Must have
• Fast loading, mobile friendly, Analytics page, email sign up link for emailed newsletter (that is not a full page pop-up but integrated into browse bar), integrated social media links, search bar, filter link, home page return link, minimalist and clean design. Formatted to product showcase website style- please see attached files for ideas for design format and word-logo.
Should not have
• No Clutter, No background advertisements, No long text scripts outside of products main page,

```html
<!DOCTYPE html>
<html lang="en">
<head>
<meta charset="utf-8">
<title>Tideloop — Home</title>
<link rel="stylesheet" href="https://fonts.googleapis.com/css2?family=Roboto:wght@400;500;700&display=swap">
<style>
:root{
  --page:#e0e0e0;
  --column:#eeeeee;
  --card:#f8f8f8;
  --ink:#222222;
  --primary:#0555a3;
  --dark:#333333;
  --footer:#353535;
  --footer-base:#303030;
  --tag:#959595;
  --footer-text:#a9a9a9;
  --footer-head:#b5b5b5;
  --bullet:#8c8c8c;
  --social-dot:#5a6b7c;
}
*{box-sizing:border-box;margin:0;padding:0}
html,body{width:1200px;height:1000px;overflow:hidden}
body{background:var(--page);font-family:"Roboto",sans-serif;position:relative}
.column{position:absolute;left:117px;top:0;width:971px;height:1000px;background:var(--column)}
.section-head{position:absolute;left:115px;width:973px;height:24px}
.section-head .rule{position:absolute;top:10px;height:4px}
.section-head h2{position:absolute;top:0;left:12px;width:100%;text-align:center;font-size:23px;font-weight:700;letter-spacing:2.5px;line-height:24px}
.section-head .nav{position:absolute;right:46px;top:2px;display:flex;gap:3px}
.trending{top:10px}
.trending .rule{background:var(--primary)}
.trending h2{color:var(--primary)}
.newstuff{top:354px}
.newstuff .rule{background:var(--dark)}
.newstuff h2{color:var(--dark)}
.rule.l{left:0;width:405px}
.rule.r{left:574px;width:302px}
.rule.end{left:938px;width:35px}
.cards{position:absolute;display:flex;gap:22px}
.cards.row1{left:148px;top:57px}
.cards.row2{left:150px;top:401px}
.card{width:210px;height:244px;background:var(--card);border-radius:8px;overflow:hidden;box-shadow:0 1px 2px rgba(0,0,0,.06)}
.card:nth-child(3){margin-left:1px}
.card .photo{height:163px;width:100%}
.card h3{font-size:18px;font-weight:500;letter-spacing:.6px;color:var(--ink);text-align:center;margin-top:13px}
.tags{display:flex;justify-content:center;gap:4px;margin-top:14px}
.tag{font-size:9px;font-weight:700;color:#fff;background:var(--tag);border-radius:4px;padding:4px 6px;line-height:10px;border:1px solid #8a8a8a}
.tag.active-blue{background:var(--primary);border-color:var(--primary)}
.tag.active-dark{background:var(--dark);border-color:var(--dark)}
.ph-promo{background:linear-gradient(160deg,#b86a5c,#9c4a42 55%,#d7cbc0)}
.ph-crew{background:linear-gradient(180deg,#4a86c8,#3d6f9e 55%,#2f3e4c)}
.ph-splash{background:radial-gradient(circle at 55% 60%,#e8ecef,#90a4b5 40%,#3c5470 85%)}
.ph-deck{background:linear-gradient(180deg,#4e86c9,#2c5f96 50%,#8a8f94)}
.site-footer{position:absolute;left:117px;top:692px;width:971px;height:248px;background:var(--footer)}
.footer-base{position:absolute;left:117px;top:940px;width:971px;height:60px;background:var(--footer-base);text-align:center;font-size:11px;letter-spacing:1.2px;color:#6c6c6c;line-height:58px}
.fcol{position:absolute;top:28px}
.fcol h4{font-size:14px;font-weight:500;letter-spacing:1.6px;color:var(--footer-head);text-align:center}
.fcol ul{list-style:none;margin-top:22px}
.fcol li{font-size:14px;color:var(--footer-text);height:27px;display:flex;align-items:center;white-space:nowrap}
.fcol li::before{content:"";flex:none;width:11px;height:11px;background:var(--bullet);margin-right:15px}
.about{left:54px;width:170px}
.products{left:275px;width:198px}
.other{left:541px;width:125px}
.social{left:752px;width:175px}
.social li::before{display:none}
.social li{height:35px;font-size:11px;font-weight:500;letter-spacing:1.3px;color:#b9b9b9}
.social .dot{flex:none;width:26px;height:26px;border-radius:50%;background:var(--social-dot);margin-right:8px}
.social ul{margin-top:16px}
.product-viewer{position:relative;margin-top:20px;width:198px;height:137px;background:#8f8f8f}
.product-viewer .photo{position:absolute;left:21px;top:10px;width:157px;height:117px}
.product-viewer svg{position:absolute;top:57px}
</style>
</head>
<body>
<div class="column"></div>

<header class="section-head trending">
  <span class="rule l"></span><span class="rule r"></span><span class="rule end"></span>
  <h2>TRENDING</h2>
  <div class="nav" aria-label="Trending navigation">
    <svg width="19" height="19" viewBox="0 0 19 19"><circle cx="9.5" cy="9.5" r="9.5" fill="#0555a3"/><path d="M12 5v9L6 9.5z" fill="#fff"/></svg>
    <svg width="19" height="19" viewBox="0 0 19 19"><circle cx="9.5" cy="9.5" r="9.5" fill="#0555a3"/><path d="M7 5v9l6-4.5z" fill="#fff"/></svg>
  </div>
</header>

<section class="cards row1">
  <article class="card"><div class="photo ph-promo" role="img" aria-label="Giveaway promotion photo with a winner holding a large cheque"></div><h3>Item Heading</h3><div class="tags"><span class="tag">#Discount</span><span class="tag">#FishHunt</span></div></article>
  <article class="card"><div class="photo ph-crew" role="img" aria-label="Fishing crew landing a marlin beside a charter boat"></div><h3>Item Heading</h3><div class="tags"><span class="tag">#Discount</span><span class="tag">#FishHunt</span></div></article>
  <article class="card"><div class="photo ph-splash" role="img" aria-label="Tuna breaking the water surface with a splash"></div><h3>Item Heading</h3><div class="tags"><span class="tag">#Discount</span><span class="tag">#FishHunt</span></div></article>
  <article class="card"><div class="photo ph-deck" role="img" aria-label="Angler on a boat deck holding a yellowfin tuna"></div><h3>Item Heading</h3><div class="tags"><span class="tag">#Discount</span><span class="tag active-blue">#FishHunt</span></div></article>
</section>

<header class="section-head newstuff">
  <span class="rule l"></span><span class="rule r"></span><span class="rule end"></span>
  <h2>NEW STUFF</h2>
  <div class="nav" aria-label="New stuff navigation">
    <svg width="19" height="19" viewBox="0 0 19 19"><circle cx="9.5" cy="9.5" r="9.5" fill="#333"/><path d="M12 5v9L6 9.5z" fill="#fff"/></svg>
    <svg width="19" height="19" viewBox="0 0 19 19"><circle cx="9.5" cy="9.5" r="9.5" fill="#333"/><path d="M7 5v9l6-4.5z" fill="#fff"/></svg>
  </div>
</header>

<section class="cards row2">
  <article class="card"><div class="photo ph-promo" role="img" aria-label="Giveaway promotion photo with a winner holding a large cheque"></div><h3>Item Heading</h3><div class="tags"><span class="tag">#Discount</span><span class="tag">#FishHunt</span></div></article>
  <article class="card"><div class="photo ph-crew" role="img" aria-label="Fishing crew landing a marlin beside a charter boat"></div><h3>Item Heading</h3><div class="tags"><span class="tag">#Discount</span><span class="tag">#FishHunt</span></div></article>
  <article class="card"><div class="photo ph-splash" role="img" aria-label="Tuna breaking the water surface with a splash"></div><h3>Item Heading</h3><div class="tags"><span class="tag">#Discount</span><span class="tag active-dark">#FishHunt</span></div></article>
  <article class="card"><div class="photo ph-deck" role="img" aria-label="Angler on a boat deck holding a yellowfin tuna"></div><h3>Item Heading</h3><div class="tags"><span class="tag">#Discount</span><span class="tag">#FishHunt</span></div></article>
</section>

<footer class="site-footer">
  <div class="fcol about">
    <h4>ABOUT US</h4>
    <ul><li>About Tideloop</li><li>Our Team</li><li>Vision</li><li>Mission</li><li>Contact</li></ul>
  </div>
  <div class="fcol products">
    <h4>PRODUCTS</h4>
    <div class="product-viewer">
      <div class="photo ph-splash" role="img" aria-label="Featured product photo of a tuna splashing"></div>
      <svg style="left:4px" width="14" height="14" viewBox="0 0 14 14"><circle cx="7" cy="7" r="7" fill="#eee"/><path d="M9 3.5v7L4.5 7z" fill="#555"/></svg>
      <svg style="left:181px" width="14" height="14" viewBox="0 0 14 14"><circle cx="7" cy="7" r="7" fill="#eee"/><path d="M5 3.5v7L9.5 7z" fill="#555"/></svg>
    </div>
  </div>
  <div class="fcol other">
    <h4>OTHER</h4>
    <ul><li>Sitemap</li><li>Privacy Policy</li><li>Code of Conduct</li><li>Affliate</li><li>Freebies</li></ul>
  </div>
  <div class="fcol social">
    <h4>SOCIAL MEDIA</h4>
    <ul>
      <li><span class="dot"></span>CHATWALL/TIDELOOP</li>
      <li><span class="dot"></span>PINBOARD/TIDELOOP</li>
      <li><span class="dot"></span>CHIRPLINE/TIDELOOP</li>
      <li><span class="dot"></span>WORKLINK/TIDELOOP</li>
    </ul>
  </div>
</footer>
<div class="footer-base">2018 © | ALL RIGHTS RESERVED</div>
</body>
</html>
```